Church Connect (post) Card
Harlow Creek Fellowship Church
Project: Church Connect (post) Card
Church Connect (post) Card - Religion and Spirituality
Creative Brief
This is a card that will be placed in bulletins at our church for the purpose of gathering information from members and guests at our church.
Front:
Title “Connect Card” followed by Church logo
Tag line: If you are a first time guest please turn your card in on the way out to receive your free gift.
“Date” followed by “Updated info” (check box)
Name –
Spouses name (if applicable)
Address
Email
Phone number
Check boxes
First time guest – 2nd time guest – regular attender - member
I’m looking for a church home – I already have a church home
How did you find out about us? ___________________________________
Back of card:
I have decided to:
(Check Boxes)
• Give my life to Jesus for the 1st time
• Recommit my life to Jesus
• Be baptized
• Transfer my membership to this church
Questions/Comments/Prayer Requests: ____________________
Stay connected at www.hcfellowship.org
Religion and Spirituality
business/church
the card needs to be creative and colorful - matching the colors of our church logo.
The size of the card needs to be 2.75 inches x 8.5 inches
double-sided
advertising for sermon series
Concepts
Peter Oakwell Ministries
Rivergate Hope Church
Lumen Ferris Cinema 12

```html
<!DOCTYPE html>
<html lang="en">
<head>
<meta charset="utf-8">
<title>Connect Card – Harlow Creek Fellowship Church</title>
<link href="https://fonts.googleapis.com/css2?family=Cinzel:wght@400;500&family=Varela+Round&family=Ubuntu:wght@400;500;700&display=swap" rel="stylesheet">
<style>
  :root{
    --stage:#111111;
    --blue:#1565b4;
    --blue-light:#2a8ad6;
    --blue-deep:#0e4f9e;
    --gold:#fbc21b;
    --gold-deep:#f4a11c;
    --paper:#ffffff;
    --ink:#555a60;
    --rule:#8a8f95;
  }
  *{margin:0;padding:0;box-sizing:border-box}
  html,body{width:1044px;height:1200px;overflow:hidden;background:var(--stage)}
  .stage{position:relative;width:1044px;height:1200px}
  .card{position:absolute;width:396px;height:1224px;transform:scale(.818);transform-origin:0 0;
        font-family:"Varela Round",sans-serif;color:var(--ink);box-shadow:4px 6px 18px rgba(0,0,0,.6)}
  .card--front{left:164px;top:93px}
  .card--back{left:584px;top:93px}
  .card__bg{position:absolute;inset:0;width:100%;height:100%}
  .card__title{position:absolute;top:36px;left:0;width:100%;text-align:center;
        font-family:"Cinzel",serif;font-weight:400;font-size:45px;color:var(--paper);letter-spacing:1px}
  .church-name{position:absolute;top:198px;left:0;width:100%;display:flex;align-items:center;justify-content:center;gap:14px}
  .church-name__dot{width:22px;height:22px;border-radius:50%;background:var(--gold)}
  .church-name__text{font-family:"Varela Round",sans-serif;font-size:22px;line-height:26px;color:var(--blue)}
  .field{position:absolute;font-size:15px;line-height:18px;white-space:nowrap;letter-spacing:.2px}
  .rule{position:absolute;height:0;border-top:1px dotted var(--rule)}
  .box{display:inline-block;width:11px;height:11px;border:1px solid var(--ink);margin-right:7px;vertical-align:-1px}
  .footer-note{position:absolute;left:0;width:100%;text-align:center;font-family:"Ubuntu",sans-serif}
  .footer-note--gift{top:1147px;font-weight:700;font-size:16px;line-height:19px;color:var(--gold);letter-spacing:-.3px}
  .footer-note--stay{top:1154px;font-size:19px;line-height:28px;color:var(--paper)}
  .footer-note__url{color:var(--gold);font-weight:700}
</style>
</head>
<body>
<div class="stage">

  <!-- Front -->
  <section class="card card--front">
    <svg class="card__bg" viewBox="0 0 396 1224" preserveAspectRatio="none" aria-hidden="true">
      <defs>
        <radialGradient id="blueFront" cx="50%" cy="0%" r="90%">
          <stop offset="0" stop-color="var(--blue-light)"/>
          <stop offset="1" stop-color="var(--blue-deep)"/>
        </radialGradient>
        <linearGradient id="goldFront" x1="0" y1="0" x2="1" y2="0">
          <stop offset="0" stop-color="var(--gold-deep)"/>
          <stop offset=".5" stop-color="var(--gold)"/>
          <stop offset="1" stop-color="var(--gold-deep)"/>
        </linearGradient>
      </defs>
      <rect width="396" height="1224" fill="url(#blueFront)"/>
      <path d="M0,168 Q198,48 396,168" fill="none" stroke="#fff" stroke-width="2"/>
      <path d="M0,170 Q198,52 396,170 L396,1071 Q198,1201 0,1071 Z" fill="url(#goldFront)"/>
      <path d="M0,190 Q198,66 396,190 L396,1046 Q198,1174 0,1046 Z" fill="#fff"/>
    </svg>
    <h1 class="card__title">Connect Card</h1>
    <div class="church-name">
      <span class="church-name__dot"></span>
      <span class="church-name__text">Harlow Creek<br>Fellowship Church</span>
    </div>

    <div class="field" style="left:23px;top:307px">Date</div>
    <div class="rule" style="left:68px;width:98px;top:322px"></div>
    <div class="field" style="left:189px;top:307px"><span class="box"></span>Update my contact info</div>

    <div class="field" style="left:23px;top:358px">Name</div>
    <div class="rule" style="left:23px;width:352px;top:407px"></div>

    <div class="field" style="left:23px;top:432px">Spouse’s name (if applicable)</div>
    <div class="rule" style="left:23px;width:352px;top:484px"></div>

    <div class="field" style="left:23px;top:508px">Address</div>
    <div class="rule" style="left:23px;width:352px;top:560px"></div>
    <div class="rule" style="left:23px;width:352px;top:606px"></div>

    <div class="field" style="left:23px;top:635px">Email</div>
    <div class="rule" style="left:23px;width:352px;top:687px"></div>

    <div class="field" style="left:23px;top:711px">Phone number</div>
    <div class="field" style="left:152px;top:711px">( <span class="box" style="margin-right:4px"></span>Cell )</div>
    <div class="rule" style="left:23px;width:352px;top:763px"></div>

    <div class="field" style="left:23px;top:794px"><span class="box"></span>1st time guest</div>
    <div class="field" style="left:235px;top:794px"><span class="box"></span>2nd time guest</div>
    <div class="field" style="left:23px;top:825px"><span class="box"></span>Regular attender</div>
    <div class="field" style="left:235px;top:825px"><span class="box"></span>Member</div>

    <div class="field" style="left:23px;top:887px"><span class="box"></span>I’m looking for a church home</div>
    <div class="field" style="left:23px;top:918px"><span class="box"></span>I already have a church home</div>

    <div class="field" style="left:23px;top:973px">How did you find out about us?</div>
    <div class="rule" style="left:23px;width:352px;top:1026px"></div>

    <p class="footer-note footer-note--gift">If you are a first time guest please turn<br>your card in on the way out to receive<br>your free gift.</p>
  </section>

  <!-- Back -->
  <section class="card card--back">
    <svg class="card__bg" viewBox="0 0 396 1224" preserveAspectRatio="none" aria-hidden="true">
      <defs>
        <radialGradient id="blueBack" cx="50%" cy="0%" r="90%">
          <stop offset="0" stop-color="var(--blue-light)"/>
          <stop offset="1" stop-color="var(--blue-deep)"/>
        </radialGradient>
        <linearGradient id="goldBack" x1="0" y1="0" x2="1" y2="0">
          <stop offset="0" stop-color="var(--gold-deep)"/>
          <stop offset=".5" stop-color="var(--gold)"/>
          <stop offset="1" stop-color="var(--gold-deep)"/>
        </linearGradient>
      </defs>
      <rect width="396" height="1224" fill="url(#blueBack)"/>
      <path d="M0,168 Q198,48 396,168" fill="none" stroke="#fff" stroke-width="2"/>
      <path d="M0,170 Q198,52 396,170 L396,1071 Q198,1201 0,1071 Z" fill="url(#goldBack)"/>
      <path d="M0,190 Q198,66 396,190 L396,1046 Q198,1174 0,1046 Z" fill="#fff"/>
    </svg>
    <h1 class="card__title">My Response</h1>
    <div class="church-name">
      <span class="church-name__dot"></span>
      <span class="church-name__text">Harlow Creek<br>Fellowship Church</span>
    </div>

    <div class="field" style="left:23px;top:357px">I have decided to:</div>
    <div class="field" style="left:23px;top:392px"><span class="box"></span>Give my life to Jesus for the 1st time</div>
    <div class="field" style="left:23px;top:419px"><span class="box"></span>Recommit my life to Jesus</div>
    <div class="field" style="left:23px;top:446px"><span class="box"></span>Be baptized</div>
    <div class="field" style="left:23px;top:474px"><span class="box"></span>Transfer my membership to this church from</div>
    <div class="field" style="left:25px;top:509px">the</div>
    <div class="rule" style="left:50px;width:270px;top:523px"></div>
    <div class="field" style="left:323px;top:509px">Church</div>
    <div class="field" style="left:23px;top:549px"><span class="box"></span></div>
    <div class="rule" style="left:42px;width:333px;top:563px"></div>

    <div class="field" style="left:23px;top:626px">Questions/Comments/Prayer Requests:</div>
    <div class="rule" style="left:23px;width:352px;top:696px"></div>
    <div class="rule" style="left:23px;width:352px;top:743px"></div>
    <div class="rule" style="left:23px;width:352px;top:791px"></div>
    <div class="rule" style="left:23px;width:352px;top:838px"></div>
    <div class="rule" style="left:23px;width:352px;top:886px"></div>
    <div class="rule" style="left:23px;width:352px;top:933px"></div>
    <div class="rule" style="left:23px;width:352px;top:980px"></div>
    <div class="rule" style="left:23px;width:352px;top:1026px"></div>

    <p class="footer-note footer-note--stay">Stay connected at<br><span class="footer-note__url">www.hcfellowship.org</span></p>
  </section>

</div>
</body>
</html>
```